Business Card for plovrix

Create a Business Card with an existing logo for plovrix AG. We are a Information Technology company that does consulting and developing SW to automate business processes. The main colors are given from the logo.

Industry/Entity Type

Business

Requirements
Nice to have
• we use a a font style Century Gothic in our documents

```html
<!DOCTYPE html>
<html lang="en">
<head>
<meta charset="utf-8">
<title>plovrix AG – Business Card</title>
<link rel="stylesheet" href="https://fonts.googleapis.com/css2?family=Questrial&family=Didact+Gothic&display=swap">
<style>
  :root {
    --bg: #2b2b2b;
    --card: #ffffff;
    --blue: #3aa6dd;
    --green: #8cc63f;
    --ink: #4a4a4a;
    --ink-dark: #3c3c3c;
    --ink-light: #6f6f6f;
    --rule: #c9c9c9;
  }
  * { margin: 0; padding: 0; box-sizing: border-box; }
  html, body { width: 1200px; height: 803px; overflow: hidden; background: var(--bg); }
  body { position: relative; font-family: "Questrial", "Didact Gothic", sans-serif; }

  .card {
    position: absolute; left: 100px; top: 116px;
    width: 1000px; height: 570px;
    background: var(--card);
    border-radius: 20px;
    overflow: hidden;
  }
  .band-top { position: absolute; left: 0; top: 0; width: 100%; height: 16px; display: flex; }
  .band-top .seg-blue { width: 42%; background: var(--blue); }
  .band-top .seg-green { flex: 1; background: var(--green); }
  .rule-top { position: absolute; left: 0; top: 22px; height: 3px; width: 100%; display: flex; }
  .rule-top .seg-blue { width: 42%; background: var(--blue); }
  .rule-top .seg-green { flex: 1; background: var(--green); }

  .band-bottom { position: absolute; left: 0; bottom: 0; width: 100%; height: 34px; display: flex; }
  .band-bottom .seg-green { width: 56%; background: var(--green); }
  .band-bottom .seg-blue { flex: 1; background: var(--blue); }

  .brand { position: absolute; left: 120px; top: 78px; display: flex; align-items: center; gap: 34px; }
  .brand-dot { width: 120px; height: 120px; border-radius: 50%; background: var(--blue); }
  .brand-name { font-size: 108px; line-height: 1; color: var(--ink); letter-spacing: 1px; }

  .person { position: absolute; left: 110px; top: 350px; width: 380px; text-align: center; }
  .person-name { font-family: "Didact Gothic", sans-serif; font-weight: 700; font-size: 44px; letter-spacing: 2px; color: var(--ink-dark); -webkit-text-stroke: 1px var(--ink-dark); }
  .person-name .surname { color: var(--ink-light); -webkit-text-stroke: 1px var(--ink-light); }
  .person-role { display: flex; align-items: center; justify-content: center; gap: 14px; margin-top: 6px; font-size: 20px; letter-spacing: 3px; color: var(--ink-light); }
  .person-role::before, .person-role::after { content: ""; width: 110px; height: 2px; background: var(--rule); }

  .contact { position: absolute; left: 535px; top: 255px; padding-left: 30px; border-left: 2px solid #e2e2e2; height: 200px; }
  .contact-row { display: flex; align-items: flex-start; gap: 18px; font-size: 25px; line-height: 31px; color: var(--ink); }
  .contact-row svg { width: 20px; height: 20px; flex: none; margin-top: 6px; fill: var(--blue); }
  .contact-row b { font-weight: 700; font-size: 18px; }
</style>
</head>
<body>
  <article class="card" aria-label="plovrix AG business card">
    <div class="band-top"><span class="seg-blue"></span><span class="seg-green"></span></div>
    <div class="rule-top"><span class="seg-blue"></span><span class="seg-green"></span></div>

    <header class="brand">
      <span class="brand-dot"></span>
      <span class="brand-name">plovrix</span>
    </header>

    <section class="person">
      <h1 class="person-name">LUKAS <span class="surname">BRENNER</span></h1>
      <p class="person-role">CEO</p>
    </section>

    <section class="contact">
      <p class="contact-row">
        <svg viewBox="0 0 24 24" aria-hidden="true"><path d="M6.6 10.8a15.1 15.1 0 0 0 6.6 6.6l2.2-2.2c.3-.3.7-.4 1-.2 1.1.4 2.3.6 3.6.6.6 0 1 .4 1 1V20c0 .6-.4 1-1 1A17 17 0 0 1 3 4c0-.6.4-1 1-1h3.5c.6 0 1 .4 1 1 0 1.3.2 2.5.6 3.6.1.3 0 .7-.2 1z"/></svg>
        <span>+41 56 000 48 20 <b>(Office)</b></span>
      </p>
      <p class="contact-row">
        <svg viewBox="0 0 24 24" aria-hidden="true"><path d="M6.6 10.8a15.1 15.1 0 0 0 6.6 6.6l2.2-2.2c.3-.3.7-.4 1-.2 1.1.4 2.3.6 3.6.6.6 0 1 .4 1 1V20c0 .6-.4 1-1 1A17 17 0 0 1 3 4c0-.6.4-1 1-1h3.5c.6 0 1 .4 1 1 0 1.3.2 2.5.6 3.6.1.3 0 .7-.2 1z"/></svg>
        <span>+41 79 000 62 17 <b>(Cell)</b></span>
      </p>
      <p class="contact-row">
        <svg viewBox="0 0 24 24" aria-hidden="true"><path d="M2 5h20v14H2z M3.5 6.5 12 13l8.5-6.5" stroke="#fff" stroke-width="1.4"/></svg>
        <span>lukas.brenner@plovrix.ch</span>
      </p>
      <p class="contact-row">
        <svg viewBox="0 0 24 24" aria-hidden="true"><circle cx="12" cy="12" r="10"/><path d="M2 12h20M12 2c3 3 3 17 0 20M12 2c-3 3-3 17 0 20" stroke="#fff" stroke-width="1.3" fill="none"/></svg>
        <span>www.plovrix.ch</span>
      </p>
      <p class="contact-row">
        <svg viewBox="0 0 24 24" aria-hidden="true"><path d="M12 2a7 7 0 0 0-7 7c0 5 7 13 7 13s7-8 7-13a7 7 0 0 0-7-7zm0 9.5A2.5 2.5 0 1 1 12 6.5a2.5 2.5 0 0 1 0 5z"/></svg>
        <span>Lindenweg 12, 5400 Baden,<br>Switzerland</span>
      </p>
    </section>

    <div class="band-bottom"><span class="seg-green"></span><span class="seg-blue"></span></div>
  </article>
</body>
</html>
```